Vel Techniqos Logo Design

We need a business card design for Las Vegas based company called "Vel Techniqs" (http://www.veltechniqs-example.com). Vel Techniqs prides itself in providing in-depth knowledge that is based on real-world experience in the field of wireless telecommunications. Our practice covers strategy, marketing, and business development across the entire telecom value chain – from consumer to enterprise, content to applications, and mobile devices to wireless infrastructure. Our expertise is in the fields of wireless telecommunications, network optimization, specializing in CDMA, UMTS, WiMAX and LTE solutions.
The logo attached could be reused for the business card, but would prefer a new innovative logo as well. The final design should project cutting edge wireless technologies. The design should also communicate a modern business that has expertise and is focused on R&D.
Updates

Team,

  Forgot to mention this.  While Vel Techniqs is focused in wireless technologies, the word 'Vel' comes from Hindi language and means harmonious music

Project Deadline Extended
Reason: Extending deadline to allow for the designer to complete final changes. Thank you all for submitting the designs so far. Thanks, Rohan.

Industry/Entity Type

Business

Logo Text

Vel Techniqs

```html
<!DOCTYPE html>
<html lang="en">
<head>
<meta charset="utf-8">
<title>Vel Techniqs business card</title>
<link rel="stylesheet" href="https://fonts.googleapis.com/css2?family=Jura:wght@500;700&display=swap">
<style>
  :root {
    --bg-top: #f3f4f6;
    --bg-bottom: #6cfcfd;
    --card: #000000;
    --card-edge: #4a4a4a;
    --brand-blue: #3d9de0;
    --mark: #6f9fbd;
    --swoosh: #a6a6a6;
    --text: #ffffff;
  }
  * { margin: 0; padding: 0; box-sizing: border-box; }
  html, body { width: 1200px; height: 1000px; overflow: hidden; }
  body {
    position: relative;
    background: linear-gradient(to bottom, var(--bg-top) 0%, var(--bg-top) 45%, var(--bg-bottom) 100%);
    font-family: "Jura", sans-serif;
  }
  .card {
    position: absolute;
    top: 210px;
    width: 376px;
    height: 563px;
    background: var(--card);
    border-left: 2px solid var(--card-edge);
    overflow: hidden;
  }
  .card--front { left: 204px; }
  .card--back { left: 621px; }
  .swoosh { position: absolute; left: 0; top: 0; }
  .brand-mark {
    position: absolute;
    border-radius: 50%;
    background: var(--mark);
  }
  .card--front .brand-mark { width: 108px; height: 108px; left: 134px; top: 226px; }
  .card--back .brand-mark { width: 96px; height: 96px; left: 140px; top: 72px; }
  .brand-name {
    position: absolute;
    left: 0; right: 0;
    text-align: center;
    color: var(--brand-blue);
    font-weight: 500;
    font-size: 27px;
    letter-spacing: 2px;
    text-transform: uppercase;
  }
  .card--front .brand-name { top: 342px; }
  .card--back .brand-name { top: 172px; }
  .contact {
    position: absolute;
    left: 0; right: 0;
    top: 396px;
    text-align: center;
    color: var(--text);
  }
  .contact__phone { font-weight: 700; font-size: 23px; margin-bottom: 14px; }
  .contact__email { font-weight: 500; font-size: 17px; margin-bottom: 16px; }
  .contact__address { font-weight: 500; font-size: 19px; line-height: 24px; }
</style>
</head>
<body>
  <section class="card card--front">
    <svg class="swoosh" width="376" height="563" viewBox="0 0 376 563" aria-hidden="true">
      <path d="M0 229 Q210 236 376 170" fill="none" stroke="var(--swoosh)" stroke-width="3"/>
      <path d="M0 249 Q220 246 376 200" fill="none" stroke="var(--swoosh)" stroke-width="3"/>
      <path d="M0 262 Q220 266 376 242 L376 287 Q220 303 0 290 Z" fill="var(--swoosh)"/>
    </svg>
    <div class="brand-mark"></div>
    <div class="brand-name">Vel Techniqs</div>
  </section>

  <section class="card card--back">
    <div class="brand-mark"></div>
    <div class="brand-name">Vel Techniqs</div>
    <div class="contact">
      <p class="contact__phone">(702) 555-0148</p>
      <p class="contact__email">Devan@veltechniqs-example.com</p>
      <p class="contact__address">48 Harmon avenue<br>Las Vegas NV 89109</p>
    </div>
  </section>
</body>
</html>
```